Website Home Page Re-Design for a Media Company producing Catholic Bible studies on CD/DVD/MP3

UPDATED BRIEF AS OF 12/28/15:

I have been in touch our rep at ArtFlock and we are going to extend this design starting on January 9. There were a couple of designs that came out ok -- I could do the tweaking on my end with the body and footer in psd -- but for every single layout the hero section is lacking. So, I guess the main thing that would create a winner is can you create an amazing hero section. I updated the brief once already truncating the focus of design elements -- I am truncating it again here to have you focus on just 1 design element -- who can create the best hero section. Something better has to be possible. I greatly appreciate your attention to this element.

UPDATED BRIEF AS OF 12/21/15:

Ladies and Gentlemen,

Thus far none of the submitted layouts fit the bill (issues being a combination of layouts, design elements, and a lot of samples with too many competing vibrant colors, etc.). So, I just finished putting together an updated template on my own (attached as updated-template.png). I am hoping that now that the layout and color scheme are firmed up (with the exceptions mentioned below), your more focused attention on the following elements will bring about a better result. For, now you are playing/manipulating just elements and not also an overall layout. Please use the bones of this updated template and focus your attention on the following while not adjusting anything not mentioned below:

Starting from the top down:

(1) I'm open to the top section with the logo/need assistance/cart icon/ etc. being manipulated around to make the Sign in and Create account links more noticeable whilst not looking crowded or forced. Not sure if things can go on different lines/different colors implemented, etc. -- that's for you to tinker with if you so choose. Keep the colors of the "Need Assistance" that turquoise blue and the phone and email icons that same orange.

(2) Still open to a better hero section. Found this to be the most disappointing part of the templates submitted thus far. I think rather than slapping images up there on a background that looks like a circus, if some real intricate time was put on making some of the CD's look very nice would help -- how to assemble them and incorporate the tag line is up to you.

(3) For the "Most Popular" and "New Releases" section, if something jumps out at you as far as how to layout the CD images that will populate this section better, I'm open. For instance, would a lighter gray background box work well behind the CD images? Would eliminating the thinly outlined rectangles around the cd images look better? Would assembling them not just in one row horizontally look better, etc.? Keep the titles and those horizontal lines on either sides of the category section the same -- but the layout of the cd images that will populate these sections are open to be modified. Keep in mind NOT TO CROWD THIS AREA -- some templates submitted just looked a mess with not enough white space, making it look very crammed and lacking distinct sections for the eye to be drawn to -- having the effect of "where do I look"?

(4) I need 3 well-designed iconic images for the Blog, Rewards Program, and Chatterly links in the gray rectangular box near the bottom. From top to bottom, the three icons combined (in total height) should be the height of the entire still frame that is situated to the left. Keep in mind, once again, space between them -- they should not looked crammed. FYI, the "Vesper Works Blog" logo as you see on our blog (vesperworksblog.example) should be a part of whatever icon you end up using.

Thank you.

INITIAL BRIEF:

1 PAGE ONLY
I am looking for a re-design of our home page at store.vesperworks.example -- you can see our current layout there. Our e-commerce store is hosted on ShopHarbor.example.

I am uploading a screen shot here of what CONTENT I would like to see on our home page, but obviously it needs to be laid out with a much more professional and polished look to -- not using the layout I currently have -- want someone who really knows what they're doing to create a really polished presentation of the CONTENT. Please pay close attention to the following considerations:

(1) As far as colors, it needs to flow well with the other pages of the website, as those will not be changes (i.e., the category pages and the product pages).

(2) I've laid out the elements in the attached design in somewhat order of importance:

(A) Visitors should see the Catch title of "Understand the Bible Like Never Before" (though this is subject to modify -- wording may be different) at the top somewhere as an eye catcher (would probably be wise to have some type of graphic like our cd covers as I have them in the screen shot, but this is definitely where your artistic talents of placement and manipulation if graphics must take over). I like the look of the cd sets in the top banner in the attached screen shot inasmuch as they look like they're stepping out of the rectangle/hero section-- obviously you can use whatever image(s) you deem appropriate and can include or exclude this design aspect -- just throwing that out there, but don't think it's mandatory if it doesn't work with the overall design.

(B) Then our most popular Bible studies section which will be populated by automated settings on the back end of shopharbor.

(C) Then our Join our email list option

(C.i.) I don't have it in the attached screen shot but we MIGHT end up doing a "Who Are We Video?" I do not know if it is possible to create the page layout such that there is room to add the image of the video still frame at some point in the future. If not just assume no video at this point.

(D) The Latest Releases is beneath the join our email list section merely because I thought there needed to be a break between having two rows of CD's merely differentiated by the title of each row (Most Popular Bible Studies vs. Latest Releases).

(E) Next is something graphically eye catching for our Blog, Chatterly and Rewards Program. Again, I just threw those images together -- not very polished or, in my estimation, very attractive -- your abilities must reign here again.

(F) Then there are what I'd call "secondary" links in the bottom horizontal black bar in the attached screen shot that are currently right beneath the bottom black bar on our current store page (e.g., Home, Services, About Us and so on). Those should be present, but obviously can be laid out in whatever design layout you envision.

(G) The Safevault, Payment Options, and "All Prices..." need to be present at the bottom too.

(H) Just noticed this -- the Search Bar obviously needs to be present as well in a noticeable way near the "Primary" links.

Again, these are just in order of importance for the most part -- they don't have to go in a perfectly lined up vertical order from top to bottom, but the eye should be drawn to the elements in roughly that order.

(2) We are looking for a clean, "elegant" home page that incorporates the elements in the attached screen shot mentioned above and doesn't look cluttered or busy.

I like the black gradient of the horizontal bars across the top and bottom in conjunction with the flesh-like gradient color of the top rectangle box/hero image -- that contrast, along with a good bit of white space works well, though I'm certainly not opposed to other color schemes -- but it has to be consonant with the other category and product pages on the website pages -- if you re-create the top section and bottom section such that the other category and product pages top and bottom sections need to be modified, that is fine if it means a much better designed home page. Not looking for a super tall page either, but it obviously will need to be taller than it currently stands at store.vesperworks.example given what we're adding to it.

(3) I don't know if there is a way to make the "Sign In" and "Create Account" more prominent at the top (or elsewhere in the design) - different fonts or fonts + icons, etc.? I think, most probably, Sign in and Create Account need to go first when read from left to right if it stayed in its current position. But, having said that, I'm not opposed to modifying the entire top section either (where our logo and the cart button currently is) if that works better with a winning design.

(4) Obviously we are eliminating the carousel of images -- only one "hero" image.

(5) Any Fonts should be clean and easy to read.

Other comments about our company:

(6) Our target audience is 25-80 year old people (yes, a broad spectrum, but I can at least say our primary audience is not teenage).

(7) Our company is dedicated to providing Catholic Bible studies on CD, DVD, and MP3.

(8) The reason why we are trying to change up the design is to try to make it more explicit what we have to offer in the first 5 seconds for those who land on our home page and do not know much about us. Trying to make it very focused on the products we offer with more image/iconic based sections of content -- e.g., as opposed to just having the text link for cd's, the blog, or the join our email list in the bottom black horizontal bar, we are dedicating a small iconic section to each of those categories.

25-80 year olds male and female

• Attached is our logo in a png format with both white background and transparent as well as in black and white and in color. You can use the text "Vesper Works" in the logo as found in the png's attached below or shifted over to the right as found at Store.vesperworks.example.
• I've attached some layouts here that I like -- obviously would want some distinct layouts, but this hopefully relays the design-type, keeping in mind the comments I've made above in the project description.

```html
<!DOCTYPE html>
<html lang="en">
<head>
<meta charset="utf-8">
<title>Vesper Works — Home</title>
<link rel="stylesheet" href="https://fonts.googleapis.com/css2?family=Open+Sans:ital,wght@0,400;0,600;1,400&family=Merriweather:ital,wght@1,700&family=Arimo&display=swap">
<style>
  :root {
    --photo-dark: #4a4541;
    --photo-mid: #857b71;
    --photo-light: #b3a799;
    --header-shade: rgba(40, 38, 36, 0.45);
    --nav-bg: rgba(44, 44, 44, 0.92);
    --nav-active: #464646;
    --white: #ffffff;
    --soft-white: #eeeeee;
    --search-bg: #cfcfcf;
    --ink: #333333;
    --body-text: #555555;
    --circle: #dddddd;
    --footer-bg: #3a3a3a;
    --footer-text: #cccccc;
    --field-border: #777777;
    --button-bg: #555555;
    --badge-bg: #f2f2f2;
    --badge-text: #444444;
    --social-bg: #222222;
    --base-bg: #1f1f1f;
    --base-text: #bbbbbb;
  }
  * { box-sizing: border-box; margin: 0; padding: 0; }
  html, body { width: 1014px; height: 1200px; overflow: hidden; }
  body { position: relative; font-family: "Open Sans", sans-serif; background: var(--white); color: var(--ink); }

  .hero-photo {
    position: absolute; left: 0; top: 0; width: 1014px; height: 543px;
    background:
      radial-gradient(ellipse at 28% 55%, rgba(150,135,118,0.55), transparent 45%),
      linear-gradient(160deg, var(--photo-dark) 0%, var(--photo-mid) 40%, var(--photo-light) 75%, var(--photo-mid) 100%);
  }
  .site-header { position: absolute; left: 0; top: 0; width: 1014px; height: 185px; background: var(--header-shade); }

  .brand { position: absolute; left: 133px; top: 40px; display: flex; align-items: center; gap: 12px; }
  .brand-mark { width: 54px; height: 54px; background: var(--white); border-radius: 6px; }
  .brand-name { color: var(--white); font-size: 24px; font-weight: 600; line-height: 28px; letter-spacing: 1px; text-transform: uppercase; }

  .account-links { position: absolute; top: 57px; left: 526px; display: flex; gap: 24px; font-size: 14px; color: var(--soft-white); }
  .search-box { position: absolute; left: 526px; top: 92px; width: 226px; height: 32px; background: var(--search-bg); border-radius: 3px; }
  .search-box span { position: absolute; left: 14px; top: 6px; font-size: 14px; font-style: italic; color: #555; }
  .search-box svg { position: absolute; right: 12px; top: 6px; }
  .cart { position: absolute; left: 772px; top: 94px; display: flex; align-items: center; gap: 10px; color: var(--soft-white); font-size: 14px; }
  .cart-icon { width: 28px; height: 28px; border-radius: 50%; background: var(--search-bg); display: flex; align-items: center; justify-content: center; }

  .main-nav { position: absolute; left: 0; top: 185px; width: 1014px; height: 50px; background: var(--nav-bg); }
  .main-nav ul { list-style: none; position: absolute; left: 129px; top: 0; display: flex; height: 50px; }
  .main-nav li { position: relative; padding: 0 12px; line-height: 48px; font-size: 14px; color: var(--soft-white); }
  .main-nav li.active { background: var(--nav-active); }
  .main-nav li.has-menu::after { content: ""; position: absolute; left: 50%; bottom: 9px; width: 5px; height: 5px; border-right: 1px solid #bbb; border-bottom: 1px solid #bbb; transform: translateX(-50%) rotate(45deg); }

  .hero-copy { position: absolute; left: 0; top: 340px; width: 1014px; text-align: center; color: var(--white); }
  .hero-title { font-family: "Merriweather", serif; font-style: italic; font-weight: 700; font-size: 27px; }
  .hero-help { margin-top: 16px; font-size: 20px; color: var(--soft-white); }
  .hero-phone { font-size: 26px; line-height: 30px; color: var(--soft-white); }

  .mission { position: absolute; left: 133px; top: 566px; width: 748px; text-align: center; }
  .mission h2 { font-size: 20px; font-weight: 400; letter-spacing: 0.5px; color: var(--ink); }
  .mission p { margin-top: 10px; font-family: "Arimo", Arial, sans-serif; font-size: 11px; line-height: 17.8px; color: var(--body-text); }

  .features { position: absolute; top: 736px; left: 0; width: 1014px; }
  .feature { position: absolute; width: 210px; text-align: center; }
  .feature-icon { width: 103px; height: 103px; border-radius: 50%; background: var(--circle); margin: 0 auto; display: flex; align-items: center; justify-content: center; }
  .feature h3 { margin-top: 10px; font-size: 20px; font-weight: 400; color: var(--ink); }
  .feature p { margin-top: 12px; font-family: "Arimo", Arial, sans-serif; font-size: 11px; line-height: 13.5px; color: var(--body-text); }

  .site-footer { position: absolute; left: 0; top: 983px; width: 1014px; height: 169px; background: var(--footer-bg); color: var(--white); }
  .footer-col { position: absolute; top: 26px; }
  .footer-col h4 { font-size: 18px; font-weight: 400; letter-spacing: 0.3px; }
  .email-field { margin-top: 14px; width: 191px; height: 33px; border: 1px solid var(--field-border); padding: 6px 13px; font-size: 13px; font-style: italic; color: var(--footer-text); }
  .subscribe { margin-top: 11px; width: 96px; height: 33px; background: var(--button-bg); border: 1px solid #666; font-size: 13px; color: var(--footer-text); line-height: 31px; text-align: center; }
  .payments { margin-top: 14px; display: grid; grid-template-columns: repeat(3, 36px); gap: 12px 22px; }
  .pay-badge { width: 36px; height: 22px; background: var(--badge-bg); border-radius: 3px; font-size: 8px; font-weight: 600; color: var(--badge-text); text-align: center; line-height: 22px; }
  .follow-text { margin-top: 11px; font-size: 13.5px; line-height: 16px; color: var(--footer-text); width: 220px; }
  .socials { margin-top: 14px; display: flex; gap: 10px; }
  .social { height: 28px; padding: 0 8px; background: var(--social-bg); border-radius: 5px; font-size: 11px; line-height: 28px; color: var(--footer-text); }

  .site-base { position: absolute; left: 0; top: 1152px; width: 1014px; height: 48px; background: var(--base-bg); text-align: center; font-size: 12px; line-height: 48px; color: var(--base-text); }
</style>
</head>
<body>
  <div class="hero-photo" role="img" aria-label="Photograph of a wooden cross on a cord resting on an open book on a wooden table"></div>

  <header class="site-header">
    <div class="brand">
      <div class="brand-mark"></div>
      <div class="brand-name">Vesper<br>Works</div>
    </div>
    <nav class="account-links">
      <span>Gift Certificates</span><span>Wishlist</span><span>Sign In</span><span>Create Account</span>
    </nav>
    <div class="search-box">
      <span>enter your keyword</span>
      <svg width="20" height="20" viewBox="0 0 20 20"><circle cx="8" cy="8" r="6.5" fill="none" stroke="#222" stroke-width="1.8"/><line x1="12.8" y1="12.8" x2="18.5" y2="18.5" stroke="#222" stroke-width="2"/></svg>
    </div>
    <div class="cart">
      <div class="cart-icon">
        <svg width="16" height="14" viewBox="0 0 16 14"><path d="M0.5 1h2.5l2 8h8l1.8-6H4" fill="none" stroke="#333" stroke-width="1.3"/><circle cx="6" cy="12" r="1.2" fill="#333"/><circle cx="12" cy="12" r="1.2" fill="#333"/></svg>
      </div>
      <span>Add to cart</span>
    </div>
  </header>

  <nav class="main-nav">
    <ul>
      <li class="active">Home</li>
      <li class="has-menu">Speaker</li>
      <li>CD</li>
      <li>DVD</li>
      <li>MP3</li>
      <li>Class</li>
      <li>Book</li>
      <li>Conference</li>
      <li class="has-menu">Category</li>
      <li>Blog</li>
      <li>Rewards Program</li>
    </ul>
  </nav>

  <section class="hero-copy">
    <h1 class="hero-title">Understand the Bible Like Never Before</h1>
    <p class="hero-help">need help?</p>
    <p class="hero-phone">(555) 014-2290</p>
  </section>

  <section class="mission">
    <h2>OUR MISSION</h2>
    <p>We want to re-fascinate the world with a message of hope. The message that once swept across entire empires like a bright and living wildfire and infectiously reconfigured people's entire worldviews, morals, and faith, has become muddled, softened, minimized, and even assaulted today. We want people to re-cognize that an old and living faith has the power to change lives, that it has historical roots that only deepen its mysterious charm and beauty, and that its truth is captivating when presented by those passionately devoted to it and well versed in Scripture and in the long Tradition, from which Scripture arose.</p>
  </section>

  <section class="features">
    <div class="feature" style="left:148px">
      <div class="feature-icon">
        <svg width="48" height="40" viewBox="0 0 48 40"><path d="M24 8C18 4 10 4 4 6v28c6-2 14-2 20 2 6-4 14-4 20-2V6c-6-2-14-2-20 2z" fill="none" stroke="#333" stroke-width="2.4" stroke-linejoin="round"/><line x1="24" y1="8" x2="24" y2="36" stroke="#333" stroke-width="2.4"/></svg>
      </div>
      <h3>Free Teachings</h3>
      <p>Lorem Ipsum is simply dummy text of the printing and typesetting industry. Lorem Ipsum standard dummy..</p>
    </div>
    <div class="feature" style="left:409px">
      <div class="feature-icon">
        <svg width="52" height="52" viewBox="0 0 52 52"><circle cx="26" cy="26" r="22" fill="none" stroke="#333" stroke-width="3.5" stroke-dasharray="5 2.5"/><circle cx="26" cy="26" r="17" fill="none" stroke="#333" stroke-width="2.5"/><text x="26" y="33" font-family="Open Sans, sans-serif" font-size="20" font-weight="600" fill="#333" text-anchor="middle">%</text></svg>
      </div>
      <h3>Exclusive Discounts</h3>
      <p>Lorem Ipsum is simply dummy text of the printing and typesetting industry. Lorem Ipsum standard dummy..</p>
    </div>
    <div class="feature" style="left:658px">
      <div class="feature-icon">
        <svg width="64" height="48" viewBox="0 0 64 48"><path d="M4 24l38-18v34L4 30z" fill="#333"/><path d="M12 30l4 10h7l-3-9" fill="none" stroke="#333" stroke-width="3"/><line x1="48" y1="10" x2="58" y2="4" stroke="#333" stroke-width="2"/><line x1="50" y1="20" x2="62" y2="18" stroke="#333" stroke-width="2"/><line x1="48" y1="30" x2="58" y2="34" stroke="#333" stroke-width="2"/></svg>
      </div>
      <h3>New Releases</h3>
      <p>Lorem Ipsum is simply dummy text of the printing and typesetting industry. Lorem Ipsum standard dummy..</p>
    </div>
  </section>

  <footer class="site-footer">
    <div class="footer-col" style="left:133px">
      <h4>NEWSLETTER</h4>
      <div class="email-field">enter email address</div>
      <div class="subscribe">SUBSCRIBE</div>
    </div>
    <div class="footer-col" style="left:383px">
      <h4>PAYMENT METHOD</h4>
      <div class="payments">
        <div class="pay-badge">Cardia</div>
        <div class="pay-badge">Merix</div>
        <div class="pay-badge">Amplex</div>
        <div class="pay-badge">Roveri</div>
        <div class="pay-badge">Paylo</div>
      </div>
    </div>
    <div class="footer-col" style="left:643px">
      <h4>FOLLOW US ON</h4>
      <p class="follow-text">You can easily add-in social icons here and a small description...</p>
      <div class="socials">
        <span class="social">Streamly</span>
        <span class="social">Clipora</span>
        <span class="social">Chatterly</span>
      </div>
    </div>
  </footer>

  <div class="site-base">All prices are in USD Copyright 2015 Vesper Works. Sitemap</div>
</body>
</html>
```